Ridgeway Ore Advisory Business Card

Ridgeway Ore Advisory is a company that provides consulting services to the Mining Industry.

Whilst Ridgeway Ore Advisory is an Australian based company its client base is the global mining industry.

The essence of Ridgeway Ore Advisory is its a can do organisation that can make a difference to its clients by providing quality assistance and form lasting relationships.
Updates

Target Market(s)

The global Mining Industry.

Industry/Entity Type

Mining

Font styles to use
Serif

Colors

Designer to choose colors to be used in the design.

Requirements
Nice to have
• My thinking is the card would look good in black given the logo.

I would like to see written on the back side of the card " Providing Metallurgical, Management and Corporate Services to the Mining Industry"

```html
<!DOCTYPE html>
<html lang="en">
<head>
<meta charset="utf-8">
<title>Ridgeway Ore Advisory – Business Card</title>
<link rel="stylesheet" href="https://fonts.googleapis.com/css2?family=Archivo:wght@400;800&family=Raleway:wght@300&display=swap">
<style>
  :root {
    --backdrop: #e6e7e9;
    --card-white: #ffffff;
    --card-black: #000000;
    --ink: #111111;
    --amber: #f9a51b;
    --white: #ffffff;
  }
  * { margin: 0; padding: 0; box-sizing: border-box; }
  html, body {
    width: 1200px;
    height: 1200px;
    overflow: hidden;
    background: var(--backdrop);
    font-family: "Archivo", Arial, sans-serif;
  }
  .card {
    position: absolute;
    left: 174px;
    width: 853px;
    height: 487px;
  }
  .card--front { top: 69px; background: var(--card-white); color: var(--ink); }
  .card--back { top: 643px; background: var(--card-black); }

  .wordmark {
    font-family: "Archivo", Arial, sans-serif;
    font-weight: 800;
    color: var(--amber);
    text-transform: uppercase;
    line-height: 1;
    letter-spacing: 0.02em;
  }
  .card--front .wordmark {
    position: absolute;
    left: 48px;
    top: 150px;
    font-size: 38px;
  }
  .card--back .wordmark {
    position: absolute;
    left: 0;
    right: 0;
    top: 175px;
    text-align: center;
    font-size: 54px;
  }

  .contact {
    position: absolute;
    left: 48px;
    top: 286px;
    list-style: none;
    font-size: 21px;
    line-height: 32.5px;
    letter-spacing: 0.01em;
  }

  .person {
    position: absolute;
    left: 502px;
    top: 142px;
  }
  .person__name {
    font-family: "Raleway", Arial, sans-serif;
    font-weight: 300;
    font-size: 45px;
    line-height: 1.1;
    letter-spacing: 0.005em;
  }
  .person__title {
    font-weight: 800;
    font-size: 22px;
    letter-spacing: 0.26em;
    margin-top: 4px;
  }

  .tagline {
    position: absolute;
    left: 0;
    right: 0;
    top: 380px;
    text-align: center;
    color: var(--amber);
    font-size: 23.5px;
    line-height: 32.5px;
  }
</style>
</head>
<body>
  <section class="card card--front" aria-label="Card front">
    <div class="wordmark">Ridgeway Ore<br>Advisory</div>
    <ul class="contact">
      <li>1375 Copperstone Road</li>
      <li>Millbrook, NJ 07012</li>
      <li>000-555-0142</li>
      <li>www.RidgewayOA.com</li>
      <li>DanielHartley@RidgewayOA.com</li>
    </ul>
    <div class="person">
      <p class="person__name">Daniel Hartley</p>
      <p class="person__title">PRESIDENT</p>
    </div>
  </section>

  <section class="card card--back" aria-label="Card back">
    <div class="wordmark">Ridgeway Ore Advisory</div>
    <p class="tagline">Providing Metallurgical, Management and<br>Corporate Services to the Mining Industry</p>
  </section>
</body>
</html>
```